DVK Webpage

We are a group dedicated to Paranormal research located in central Mississippi .. we are looking for an index page and a blank template so we can fill in and finish the rest. Would like links to include, Home, About us, Research, Contact us and More.. kind of like the look of the image uploaded .. also included is our logo

```html
<!DOCTYPE html>
<html lang="en">
<head>
<meta charset="utf-8">
<title>DVK Paranormal Investigation</title>
<link href="https://fonts.googleapis.com/css2?family=Gentium+Book+Plus:wght@400;700&display=swap" rel="stylesheet">
<style>
  :root {
    --ink: #050505;
    --night: #0b0b0b;
    --smoke: #2a2a2a;
    --smoke-light: #3a3a3a;
    --text: #e6e6e6;
    --text-soft: #c9c9c9;
    --gold: #d8c39a;
    --button: #3b3b3b;
    --rule: #6d6d6d;
    --frame: #3c3c3c;
  }
  * { margin: 0; padding: 0; box-sizing: border-box; }
  html, body { width: 1200px; height: 2432px; overflow: hidden; }
  body {
    position: relative;
    background: var(--ink);
    color: var(--text);
    font-family: "Gentium Book Plus", Georgia, serif;
  }
  a { color: inherit; text-decoration: none; }

  /* Hero */
  .hero { position: absolute; left: 0; top: 0; width: 1200px; height: 700px; }
  .hero-photo {
    position: absolute; inset: 0;
    background: linear-gradient(180deg, #121212 0%, #2e2e2e 40%, #3a3a3a 62%, #262626 82%, #2c2c2c 100%);
  }
  .hero-title {
    position: absolute; left: 0; top: 366px; width: 1200px;
    text-align: center; font-size: 39px; line-height: 51px; font-weight: 400;
    letter-spacing: .5px; color: #f2f2f2; text-transform: uppercase;
  }
  .slider-dots {
    position: absolute; top: 675px; left: 582px; display: flex; gap: 7px;
  }
  .slider-dots span { width: 8px; height: 8px; border-radius: 50%; background: #fff; }

  /* Navigation */
  .site-nav {
    position: absolute; left: 0; top: 0; width: 1200px; height: 109px;
    background: rgba(8,8,8,.88);
  }
  .nav-link {
    position: absolute; top: 48px; font-size: 19px; color: #fff; text-transform: uppercase;
  }
  .nav-link.is-active { color: var(--gold); }
  .brand-badge { position: absolute; left: 512px; top: 0; width: 176px; height: 203px; }
  .brand-name {
    position: absolute; left: 512px; top: 70px; width: 176px; text-align: center;
    font-size: 30px; color: var(--gold); letter-spacing: 2px;
  }

  /* Welcome */
  .welcome {
    position: absolute; left: 0; top: 700px; width: 1200px; height: 520px;
    background: linear-gradient(180deg, #262626 0%, var(--smoke-light) 50%, #2a2a2a 100%);
  }
  .welcome-heading {
    position: absolute; left: 100px; top: 730px; width: 461px; text-align: right;
    font-size: 36px; line-height: 48px; font-weight: 400; text-transform: uppercase;
  }
  .welcome-photo {
    position: absolute; left: 112px; top: 894px; width: 441px; height: 253px;
    border: 2px solid var(--frame);
    background: linear-gradient(135deg, #4a5a6e 0%, #26344a 45%, #0c121b 100%);
  }
  .welcome-rule { position: absolute; left: 594px; top: 741px; width: 1px; height: 406px; background: var(--rule); }
  .welcome-copy { position: absolute; left: 616px; top: 740px; width: 490px; }
  .welcome-copy p { font-size: 13px; line-height: 20.6px; color: var(--text-soft); margin-bottom: 20px; }
  .button {
    display: inline-block; background: var(--button); color: #fff;
    font-size: 12px; text-align: center; line-height: 29px;
  }
  .welcome-copy .button { width: 107px; margin-top: -6px; }

  /* Investigations */
  .investigations { position: absolute; left: 0; top: 1190px; width: 1200px; height: 600px; background: var(--night); }
  .section-title {
    position: absolute; left: 0; width: 1200px; text-align: center;
    font-size: 37px; font-weight: 400; text-transform: uppercase; color: #fff;
  }
  .case-card { position: absolute; top: 1359px; width: 308px; }
  .case-photo { width: 308px; height: 184px; border: 3px solid var(--frame); }
  .case-title { margin-top: 24px; font-size: 12.5px; text-transform: uppercase; font-weight: 400; color: #fff; }
  .case-text { margin-top: 14px; font-size: 11px; line-height: 20.5px; color: var(--text-soft); }
  .case-card .button { width: 94px; height: 27px; line-height: 27px; margin-top: 14px; font-size: 11px; }

  /* Testimonials */
  .testimonials {
    position: absolute; left: 0; top: 1770px; width: 1200px; height: 480px;
    background: linear-gradient(180deg, #1d1d1d 0%, var(--smoke) 40%, #1a1a1a 100%);
  }
  .quote { position: absolute; top: 1948px; width: 310px; }
  .quote-mark { font-size: 50px; line-height: 30px; height: 30px; color: #fff; }
  .quote-text { margin-top: 12px; font-size: 14.5px; line-height: 20.5px; color: #f0f0f0; }
  .quote-author { margin-top: 12px; display: flex; align-items: center; gap: 8px; }
  .avatar { width: 42px; height: 42px; border-radius: 50%; background: linear-gradient(135deg, #8a8a8a, #4a4a4a); }
  .author-name { font-size: 19px; line-height: 20px; color: #c9c9c9; }
  .author-city { font-size: 11px; color: #e0e0e0; }

  /* Footer */
  .site-footer { position: absolute; left: 0; top: 2250px; width: 1200px; height: 182px; background: var(--ink); }
  .social { position: absolute; top: 2275px; width: 36px; height: 36px; border: 2px solid #fff; border-radius: 50%; }
  .footer-links {
    position: absolute; top: 2326px; left: 0; width: 1200px; text-align: center; font-size: 14px; color: #fff;
  }
  .footer-links span { margin: 0 6px; }
  .copyright { position: absolute; top: 2358px; left: 0; width: 1200px; text-align: center; font-size: 12px; color: #ddd; }
</style>
</head>
<body>

<header class="hero">
  <div class="hero-photo" role="img" aria-label="Night photograph of an abandoned house under a full moon"></div>
  <h1 class="hero-title">DVK Paranormal<br>Investigation</h1>
  <div class="slider-dots"><span></span><span></span><span></span><span></span></div>
</header>

<nav class="site-nav">
  <a class="nav-link is-active" href="#" style="left:238px">Home</a>
  <a class="nav-link" href="#" style="left:336px">About Us</a>
  <a class="nav-link" href="#" style="left:715px">Research</a>
  <a class="nav-link" href="#" style="left:852px">Contact Us</a>
</nav>
<svg class="brand-badge" viewBox="0 0 176 203" aria-hidden="true">
  <polygon points="0,0 176,0 176,115 88,203 0,115" fill="#0a0a0a"/>
</svg>
<div class="brand-name">DVK</div>

<section class="welcome"></section>
<h2 class="welcome-heading">Welcome to<br>DVK Paranormal<br>Investigation</h2>
<div class="welcome-photo" role="img" aria-label="Photograph of a castle silhouette against a moonlit cloudy sky"></div>
<div class="welcome-rule"></div>
<div class="welcome-copy">
  <p>Lorem Ipsum is simply dummy text of the printing and typesetting industry. Lorem Ipsum has been the industry's standard dummy text ever since the 1500s, when an unknown printer took a galley of type and scrambled it to make a type specimen book. It has survived not only five centuries, but also the leap into electronic typesetting, remaining essentially unchanged. It was popularised in the 1960s with the release of Letraset sheets containing .</p>
  <p>Lorem Ipsum is simply dummy text of the printing and typesetting industry. Lorem Ipsum has been the industry's standard dummy text ever since the 1500s, when an unknown printer took a galley of type and scrambled it to make a type specimen book. It has survived not only five centuries, but also the leap into electronic typesetting, remaining essentially unchanged. It was popularised in the 1960s with the release of Letraset sheets containing Lorem Ipsum passages, and more recently with desktop publishing software like Aldus PageMaker including versions of Lorem Ipsum. Lorem Ipsum is simply dummy text of the printing and typesetting industry. Lorem Ipsum has been the industry's standard dummy text ever since the 1500s, when an unknown printer took a galley of type and scrambled it to make a type specimen book. It has survived not only five centuries ...</p>
  <a class="button" href="#">Read More</a>
</div>

<section class="investigations"></section>
<h2 class="section-title" style="top:1266px">Our Recent Investigations</h2>

<article class="case-card" style="left:112px">
  <div class="case-photo" role="img" aria-label="Photograph of an investigator in a suit holding a magnifying glass and notebook" style="background:linear-gradient(135deg,#1c2436,#3a4660 55%,#10141e)"></div>
  <h3 class="case-title">DVK Paranormal Investigation</h3>
  <p class="case-text">Lorem Ipsum is simply dummy text of the printing and typesetting industry. Lorem Ipsum has been the industry's standard dummy text ever since the 1500s</p>
  <a class="button" href="#">View Details</a>
</article>
<article class="case-card" style="left:446px">
  <div class="case-photo" role="img" aria-label="Photograph of yellow crime scene tape among leaves" style="background:linear-gradient(160deg,#2c3a22 0%,#6a6a2a 40%,#b8a82a 55%,#3c4a24 80%)"></div>
  <h3 class="case-title">DVK Paranormal Investigation</h3>
  <p class="case-text">Lorem Ipsum is simply dummy text of the printing and typesetting industry. Lorem Ipsum has been the industry's standard dummy text ever since the 1500s</p>
  <a class="button" href="#">View Details</a>
</article>
<article class="case-card" style="left:780px">
  <div class="case-photo" role="img" aria-label="Photograph of a forensic investigator with a flashlight examining evidence" style="background:linear-gradient(135deg,#14182a,#2e3350 55%,#5a5468)"></div>
  <h3 class="case-title">DVK Paranormal Investigation</h3>
  <p class="case-text">Lorem Ipsum is simply dummy text of the printing and typesetting industry. Lorem Ipsum has been the industry's standard dummy text ever since the 1500s</p>
  <a class="button" href="#">View Details</a>
</article>

<section class="testimonials"></section>
<h2 class="section-title" style="top:1836px">Testimonials</h2>

<blockquote class="quote" style="left:112px">
  <div class="quote-mark">&ldquo;</div>
  <p class="quote-text">Lorem Ipsum is simply dummy text of the printing and typesetting industry. Lorem Ipsum has been the industry's standard dummy text ever since the 1500s</p>
  <div class="quote-author"><div class="avatar" role="img" aria-label="Client portrait"></div><div><div class="author-name">Daniel Harwick</div><div class="author-city">London</div></div></div>
</blockquote>
<blockquote class="quote" style="left:446px">
  <div class="quote-mark">&ldquo;</div>
  <p class="quote-text">Lorem Ipsum is simply dummy text of the printing and typesetting industry. Lorem Ipsum has been the industry's standard dummy text ever since the 1500s</p>
  <div class="quote-author"><div class="avatar" role="img" aria-label="Client portrait"></div><div><div class="author-name">Daniel Harwick</div><div class="author-city">London</div></div></div>
</blockquote>
<blockquote class="quote" style="left:780px">
  <div class="quote-mark">&ldquo;</div>
  <p class="quote-text">Lorem Ipsum is simply dummy text of the printing and typesetting industry. Lorem Ipsum has been the industry's standard dummy text ever since the 1500s</p>
  <div class="quote-author"><div class="avatar" role="img" aria-label="Client portrait"></div><div><div class="author-name">Daniel Harwick</div><div class="author-city">London</div></div></div>
</blockquote>

<footer class="site-footer"></footer>
<a class="social" href="#" aria-label="Social link" style="left:561px"></a>
<a class="social" href="#" aria-label="Social link" style="left:603px"></a>
<div class="footer-links">
  <a href="#">Home</a><span>|</span><a href="#">About us</a><span>|</span><a href="#">Research</a><span>|</span><a href="#">Contact Us</a>
</div>
<div class="copyright">&copy; 2015 Company Name , All Rights Reserved</div>

</body>
</html>
```